Flyer for GIS workshop

We need a 2 page flyer for a technology workshop for non-techies. The participants will be older farmers, land and agriculture business owners who are not tech savvy.

A bonus will be awarded to the designer that thinks of a catchy name for the workshop

Please see the following doc for the text. Some words may change but not the number of words.

https://pages.brellomix.net/sheet/q/8k24RT7wPbnMxC51QdLzkUyVRoeTa7JhWcNsp3Xf04/view?share=opened

I have attached the organisation logo.

The organisation website is www.tarwelo.org , please have a look at our old flyers (this is not professional design, we expect a lot better from participants). The new website is professionally designed and the flyer needs to have a complimentary concept.

FINAL OUTPUT
1. We need this in any opensource design software -it just needs to be free for commercial use. Some options are Scribus, Inkscape, GIMP etc.
2. All images used must be creative commons
3. The front page must be able to be used without the back (we will print this at A3 or bigger for pasting on walls)

IMPORTANT
Selected designer will be asked to work on future layouts for multiple events held every few months.

The participants will be older farmers, land and agriculture business owners who are not tech savvy.

Agriculture

• Final product in any opensource design software -it just needs to be free for commercial use. Some options are Scribus, Inkscape, GIMP etc.
2 pages A4
Front page must be able to be printed at larger size and placed in shop windows or reduced in size for newspapers with minimal re-design
• Include Creative Common images

```html
<!DOCTYPE html>
<html lang="en">
<head>
<meta charset="utf-8">
<title>Techmac Savvy – GIS Workshop Flyer</title>
<link href="https://fonts.googleapis.com/css2?family=Bebas+Neue&family=Open+Sans:wght@400;600;700&display=swap" rel="stylesheet">
<style>
:root{
  --dark:#2a7a2f;
  --mid:#4f9a2c;
  --light:#8dc63f;
  --yellow:#f6e24a;
  --ink:#3a3a3a;
  --bg:#2b2b2b;
  --white:#ffffff;
}
*{box-sizing:border-box;margin:0;padding:0}
html,body{width:1200px;height:823px;overflow:hidden;background:var(--bg)}
body{position:relative;font-family:"Open Sans",Arial,sans-serif;color:var(--ink)}
.page{position:absolute;top:48px;width:514px;height:720px;background:var(--white);overflow:hidden;box-shadow:0 6px 18px rgba(0,0,0,.5)}
.page--front{left:60px}
.page--back{left:633px}
.abs{position:absolute}
.top-stripe{left:0;top:0;width:100%;height:8px;display:flex}
.top-stripe span{flex:1}
.photo{position:absolute}
.brand-tab{position:absolute;background:var(--white);clip-path:polygon(0 0,100% 0,100% 78%,50% 100%,0 78%);display:flex;align-items:flex-start;justify-content:center;gap:8px}
.brand-name{font-family:"Open Sans",Arial,sans-serif;font-weight:700;color:var(--dark);letter-spacing:.5px}
.brand-dot{border-radius:50%;background:var(--dark)}
.q-box{position:absolute;top:312px;height:94px;color:var(--white);font-weight:700;font-size:11.5px;line-height:1.25;text-align:center;display:flex;align-items:center;justify-content:center;padding:0 8px}
.cost-col{position:absolute;left:351px;top:302px;width:163px;height:384px;background:var(--dark)}
.hex{position:absolute;left:360px;top:300px;width:138px;height:142px;background:var(--white);clip-path:polygon(25% 0,75% 0,100% 50%,75% 100%,25% 100%,0 50%)}
.hex-photo{position:absolute;left:366px;top:306px;width:126px;height:130px;clip-path:polygon(25% 0,75% 0,100% 50%,75% 100%,25% 100%,0 50%);background:linear-gradient(135deg,#dfe6ea,#6a8fa6 60%,#3b4b55)}
.cost-head{position:absolute;left:362px;top:478px;width:146px;font-family:"Bebas Neue",Impact,sans-serif;color:var(--white);font-size:25px;line-height:1.0}
.cost-offer{position:absolute;left:362px;top:586px;width:146px;font-weight:600;color:#e8f5d4;font-size:14.5px;line-height:1.2}
.cost-offer b{color:var(--yellow);font-size:17px}
.title{position:absolute;left:8px;top:412px;width:335px;text-align:center;white-space:nowrap;font-family:"Bebas Neue",Impact,sans-serif;font-weight:400;font-size:60px;line-height:1;color:var(--mid);-webkit-text-stroke:1.5px var(--dark)}
.ribbon{position:absolute;left:28px;top:484px;width:290px;height:30px;background:var(--dark);clip-path:polygon(0 0,100% 0,96% 50%,100% 100%,0 100%,4% 50%);color:var(--white);font-size:20px;font-weight:600;text-align:center;line-height:30px;white-space:nowrap}
.ticks{position:absolute;left:14px;top:526px;width:322px;list-style:none;font-size:11.2px;line-height:1.3}
.ticks li{display:flex;gap:7px;margin-bottom:8px}
.ticks svg{flex:none;margin-top:1px}
.address-bar{position:absolute;left:14px;top:641px;width:322px;height:26px;background:var(--dark);clip-path:polygon(4% 0,100% 0,100% 100%,4% 100%,0 50%);color:var(--white);display:flex;align-items:center;gap:6px;padding-left:22px;font-size:11px;font-weight:600;white-space:nowrap}
.address-bar .phone{font-family:"Bebas Neue",Impact,sans-serif;font-size:18px;font-weight:400;display:flex;align-items:center;gap:4px;margin-left:4px}
.foot{position:absolute;left:0;top:683px;width:100%;height:37px;display:flex}
.foot div{display:flex;align-items:center;gap:7px;color:var(--white);font-weight:700;font-size:13px;padding-left:16px;white-space:nowrap}
.foot .big{font-family:"Bebas Neue",Impact,sans-serif;font-size:24px;font-weight:400}
.info-box{position:absolute;top:268px;height:99px;color:var(--white);font-size:6.3px;line-height:1.35;text-transform:uppercase;text-align:center;display:flex;align-items:center;justify-content:center;padding:0 8px}
.side-col{position:absolute;left:0;top:376px;width:164px;height:307px;background:var(--light);color:var(--white);font-size:9.6px;font-weight:700;line-height:1.2;padding:7px 10px}
.back-copy{position:absolute;left:175px;width:330px;font-size:11px;line-height:1.35}
.back-copy strong{color:var(--dark)}
.muted{color:#555;font-weight:600}
.tag{position:absolute;left:164px;height:24px;background:var(--light);clip-path:polygon(0 0,93% 0,100% 50%,93% 100%,0 100%);color:var(--white);font-weight:700;display:flex;align-items:center;padding-left:12px;white-space:nowrap}
.link{color:var(--dark);font-weight:700;font-size:10.5px;line-height:1.3}
</style>
</head>
<body>

<section class="page page--front">
  <div class="abs top-stripe"><span style="background:var(--mid)"></span><span style="background:var(--dark)"></span><span style="background:var(--light)"></span></div>
  <div class="photo" role="img" aria-label="Rider on a brown horse on a farm track beside a paddock fence" style="left:0;top:8px;width:514px;height:310px;background:linear-gradient(160deg,#c9d6d8 0%,#8e9a7a 40%,#6b4a32 70%,#a58b6a 100%)"></div>
  <div class="brand-tab" style="left:23px;top:8px;width:231px;height:124px;padding-top:30px">
    <span class="brand-name" style="font-size:34px">Tarwelo</span>
    <span class="brand-dot" style="width:14px;height:14px;margin-top:18px"></span>
  </div>

  <div class="q-box" style="left:0;width:122px;background:var(--dark)">Do you want to visualise your agricultural environment and workflows?</div>
  <div class="q-box" style="left:122px;width:120px;background:var(--mid)">Do you want to reduce your inputs and increase your yields?</div>
  <div class="q-box" style="left:242px;width:112px;background:var(--light)">Have you heard of Geographical Information Systems (GIS)?</div>

  <div class="cost-col"></div>
  <div class="hex"></div>
  <div class="hex-photo" role="img" aria-label="Hands holding a tablet showing a map"></div>

  <h1 class="title">TECHMAC SAVVY</h1>
  <div class="ribbon">who are not tech savvy</div>

  <ul class="ticks">
    <li><svg width="12" height="12" viewBox="0 0 12 12"><path d="M1 6l3.5 4L11 1.5" fill="none" stroke="#8dc63f" stroke-width="2.2"/></svg><span>The Tarwelo GIS Network (TARWELO) is organising a weekend program at Brindaroo Station near Kelvale from 28th to 30th of November 2014.</span></li>
    <li><svg width="12" height="12" viewBox="0 0 12 12"><path d="M1 6l3.5 4L11 1.5" fill="none" stroke="#8dc63f" stroke-width="2.2"/></svg><span>Without having to fly or travel too far</span></li>
    <li><svg width="12" height="12" viewBox="0 0 12 12"><path d="M1 6l3.5 4L11 1.5" fill="none" stroke="#8dc63f" stroke-width="2.2"/></svg><span>Join Us and get on the road to technology<br>that will save you !</span></li>
  </ul>

  <div class="address-bar">PO Box 2710 Marlow, QLD 4890
    <span class="phone"><svg width="13" height="13" viewBox="0 0 14 14"><rect x="0" y="0" width="14" height="14" rx="3" fill="#fff"/><path d="M4 3l2 2-1 1.5c.6 1.2 1.4 2 2.5 2.5L9 8l2 2-1.2 1.3C6.5 11 3 7.5 2.7 4.2z" fill="#2a7a2f"/></svg>123-555-4180</span>
  </div>

  <div class="cost-head">DO YOU THINK TO<br>USE A GIS WILL<br>COST YOU<br>LOTS OF $$$?</div>
  <div class="cost-offer">How about only <b>$350</b> to learn some of it yourself in a weekend?</div>

  <div class="foot">
    <div style="width:181px;background:var(--dark)"><svg width="13" height="13" viewBox="0 0 14 14" fill="none" stroke="#fff" stroke-width="1.2"><circle cx="7" cy="7" r="6"/><ellipse cx="7" cy="7" rx="2.6" ry="6"/><path d="M1 7h12"/></svg>www.tarwelo.org</div>
    <div style="width:170px;background:var(--mid)"><svg width="15" height="11" viewBox="0 0 15 11"><rect width="15" height="11" fill="#fff"/><path d="M0 0l7.5 6L15 0" fill="none" stroke="#4f9a2c" stroke-width="1.3"/></svg>admin@tarwelo.org</div>
    <div class="big" style="flex:1;background:var(--light)"><svg width="16" height="16" viewBox="0 0 14 14"><rect width="14" height="14" rx="3" fill="#fff"/><path d="M4 3l2 2-1 1.5c.6 1.2 1.4 2 2.5 2.5L9 8l2 2-1.2 1.3C6.5 11 3 7.5 2.7 4.2z" fill="#8dc63f"/></svg>123-555-4180</div>
  </div>
</section>

<section class="page page--back">
  <div class="abs top-stripe"><span style="background:var(--dark)"></span><span style="background:var(--light)"></span><span style="background:var(--dark)"></span></div>
  <div class="photo" role="img" aria-label="Farmer using a laptop in a wheat field with a harvester behind" style="left:0;top:8px;width:514px;height:254px;background:linear-gradient(180deg,#9ec3e6 0%,#dfe9f2 35%,#c9ad6e 60%,#b89452 100%)"></div>
  <div class="brand-tab" style="left:297px;top:8px;width:208px;height:94px;padding-top:24px">
    <span class="brand-name" style="font-size:27px">Tarwelo</span>
    <span class="brand-dot" style="width:11px;height:11px;margin-top:14px"></span>
  </div>

  <div class="info-box" style="left:0;width:164px;background:var(--dark)">The Tarwelo GIS Network (TARWELO) are a volunteer group of geographical information system (GIS) officers and surveyors that want to help promote GIS in North Queensland.</div>
  <div class="info-box" style="left:172px;width:169px;background:var(--mid)">The term, geographical information system (GIS) is a computer system designed to capture, store, manipulate, analyse, manage, and present all types of geographical (aka spatial) data.</div>
  <div class="info-box" style="left:349px;width:165px;background:var(--dark);font-size:5.6px">To present data collected by downloading free (open) spatial data or integrating GPS collected data, a commercial software system used to be required. This has meant expensive training courses and purchasing software licenses. Commercial software ranges in price from $8,000 to over $20,000. Fortunately, open source software is now available to fulfill at least the basic requirements, and what's better - it's absolutely free.</div>

  <div class="side-col">TARWELO is holding a three day workshop at Brindaroo Station, from 28th to 30th November 2014, to show non spatial people how to use this freely available software. Maps produced can be anything from recording where someone has been on their holiday to identifying the spread of weeds on a property, fire management, optimum positions for trapping feral animals or counting grass to uncover the most economical and sustainable grazing system for a property.</div>

  <div class="back-copy muted" style="top:382px;font-size:11.5px">To book your accommodation at Brindaroo Station, go to:</div>
  <div class="back-copy" style="top:402px"><strong>www.brindaroostation.com.au</strong> and tell them that you are with Tarwelo to get a special rate. Attendees can also stay in many motels and campsites in Mt Ardell, Coreen Hot Springs and Kelvale which are less than 20mins away.</div>

  <div class="tag" style="top:484px;width:156px;font-size:16px">References</div>
  <div class="back-copy link" style="top:518px">http://www.mapcraft-demo.org/library/ebooks/farming-the-future.pdf</div>
  <div class="back-copy link" style="top:550px">http://www.geofieldnotes.com/agriculture-and-gis/</div>
  <div class="back-copy muted" style="top:572px">To register your interest in attending this free training, and view the program go to:</div>
  <div class="tag" style="top:610px;width:250px;font-size:13px">www.tarwelo.org/workshops/XXX</div>
  <div class="back-copy muted" style="top:642px">PO Box 2710 Marlow, QLD 4890</div>
  <div class="back-copy" style="top:656px;font-family:'Bebas Neue',Impact,sans-serif;font-size:19px;color:var(--dark);display:flex;align-items:center;gap:5px"><svg width="13" height="13" viewBox="0 0 14 14"><rect width="14" height="14" rx="3" fill="#2a7a2f"/><path d="M4 3l2 2-1 1.5c.6 1.2 1.4 2 2.5 2.5L9 8l2 2-1.2 1.3C6.5 11 3 7.5 2.7 4.2z" fill="#fff"/></svg>123-555-4180</div>

  <div class="foot">
    <div style="width:164px;background:var(--dark)"><svg width="13" height="13" viewBox="0 0 14 14" fill="none" stroke="#8dc63f" stroke-width="1.2"><circle cx="7" cy="7" r="6"/><ellipse cx="7" cy="7" rx="2.6" ry="6"/><path d="M1 7h12"/></svg>www.tarwelo.org</div>
    <div style="width:185px;background:var(--mid)"><svg width="15" height="11" viewBox="0 0 15 11"><rect width="15" height="11" fill="#fff"/><path d="M0 0l7.5 6L15 0" fill="none" stroke="#4f9a2c" stroke-width="1.3"/></svg>admin@tarwelo.org</div>
    <div class="big" style="flex:1;background:var(--dark)"><svg width="15" height="15" viewBox="0 0 14 14"><rect width="14" height="14" rx="3" fill="#fff"/><path d="M4 3l2 2-1 1.5c.6 1.2 1.4 2 2.5 2.5L9 8l2 2-1.2 1.3C6.5 11 3 7.5 2.7 4.2z" fill="#2a7a2f"/></svg>123-555-4180</div>
  </div>
</section>

</body>
</html>
```